Hockey Habits Poster Board for a Girls Youth Hockey Team

I'd like to have a (2) sided poster board created for our hockey team. The poster board will be 2'x4'. There are (4) different types of team play as follows:

Offense w/Puck - You have the puck and your team is on offense
-------------
Offense wo/Puck - You do not have the puck but your teammate does
-------------
Defense on/Puck - Your opponent has the puck and you are the closest defender from your team to the opponent with the puck
-------------
Defense away/Puck - Your opponent has the puck and you are not the closes defender from your team to the opponent with the puck
--------------
Individual habits are what we want every player to have regardless of the team situation. I think I'd like to have the individual habits on both sides of the poster board.

I'm open to ideas but I thought it would be cool to have a hockey rink in the background. This is also for a girls hockey team so if you are going to use a hockey player - please make sure the player is female.

Target Market(s)

Youth Hockey

Industry/Entity Type

Youth Sports - Hockey

Font styles to use
Serif
Sans Serif

Colors
0054AA
0677BA
7BADD7
CADEEF
E8F1F8
00AB8E
00BBA5
67D7C9
C6EFE9
E9F9F6

Requirements
Must have
• All of the individual habits on both sides. All the defensive habits on one side and the offensive habits on the other side.
Nice to have
• I'd like to see an image of a hockey rink on both sides of the poster as well as a female hockey player
Should not have
• boys

```html
<!DOCTYPE html>
<html lang="en">
<head>
<meta charset="utf-8">
<title>Hockey Habits</title>
<link href="https://fonts.googleapis.com/css2?family=Russo+One&family=Audiowide&family=Roboto+Condensed:wght@400;700&display=swap" rel="stylesheet">
<style>
  :root{
    --ink:#2b2b2b;
    --muted:#555;
    --panel:#eef0f4;
    --white:#ffffff;
    --red:#e05858;
    --red-soft:#ef9b9b;
    --gold:#d4b24a;
    --gold-soft:#f3d98a;
    --green:#7cc36a;
    --green-soft:#a8e58d;
    --purple:#c055e2;
    --blue:#4c86e2;
  }
  *{box-sizing:border-box;margin:0;padding:0}
  html,body{width:1200px;height:2400px;overflow:hidden;background:var(--white)}
  body{position:relative;font-family:"Roboto Condensed",Arial,sans-serif;color:var(--ink)}

  .hero{position:absolute;left:0;top:0;width:1200px;height:600px;overflow:hidden}
  .hero-scene{position:absolute;inset:0;
    background:
      radial-gradient(ellipse 60% 40% at 50% 52%, rgba(190,225,255,.55), transparent 70%),
      radial-gradient(ellipse 30% 60% at 92% 45%, rgba(10,25,60,.85), transparent 70%),
      linear-gradient(180deg,#040a1e 0%,#0b2c6e 30%,#2b6fc2 52%,#8fc0ea 72%,#d7e8f7 88%,#eef4fb 100%)}
  .hero-ice{position:absolute;left:-60px;right:-60px;top:540px;height:160px;background:var(--white);border-radius:50% 50% 0 0/40% 40% 0 0}
  .hero-title{position:absolute;left:150px;top:170px;width:800px;font-family:"Russo One",sans-serif;color:var(--white);
    line-height:1;text-transform:uppercase;paint-order:stroke fill}
  .hero-title .line1{display:block;font-size:150px;letter-spacing:4px;-webkit-text-stroke:12px #c21a3a;text-shadow:0 4px 10px rgba(0,0,0,.4)}
  .hero-title .line2{display:block;font-size:150px;letter-spacing:6px;margin-top:16px;padding-left:44px;-webkit-text-stroke:12px #e08a20;text-shadow:0 4px 10px rgba(0,0,0,.3)}

  .pill{position:absolute;border-radius:26px;display:flex;align-items:center;justify-content:center;gap:18px;color:var(--white);
    box-shadow:0 14px 14px -10px rgba(0,0,0,.35)}
  .pill .pill-name{font-family:"Russo One",sans-serif;font-size:31px;letter-spacing:1px;text-transform:uppercase}
  .pill .pill-note{font-size:26px}
  .pill-individual{left:403px;top:578px;width:404px;height:43px;background:var(--red)}
  .pill-offense-puck{left:178px;top:1174px;width:910px;height:44px;background:var(--purple)}
  .pill-offense-nopuck{left:116px;top:1789px;width:990px;height:44px;background:var(--blue)}

  .skills{position:absolute;left:0;width:1200px}
  .skill{position:absolute;transform:translateX(-50%);display:flex;flex-direction:column;align-items:center;white-space:nowrap}
  .skill svg{width:56px;height:56px;margin-bottom:14px}
  .skill-label{font-weight:700;font-size:19px;text-transform:uppercase;color:var(--ink)}
  .divider{position:absolute;width:2px;height:15px}
  .skills-individual{top:650px} .skills-individual .divider{top:71px;background:var(--red)}
  .skills-individual svg{fill:var(--red)}
  .skills-offense-puck{top:1255px} .skills-offense-puck .divider{top:77px;background:var(--purple)}
  .skills-offense-puck svg{fill:var(--purple)}
  .skills-offense-nopuck{top:1884px} .skills-offense-nopuck .divider{top:70px;background:var(--blue)}
  .skills-offense-nopuck svg{fill:var(--blue)}

  .tier{position:absolute;left:34px;width:1135px;background:var(--panel);box-shadow:0 3px 6px rgba(0,0,0,.12)}
  .tier-middle{position:absolute;top:0;bottom:0;left:335px;width:421px;background:var(--white)}
  .grade{position:absolute;top:18px}
  .grade-head{height:38px;display:flex;align-items:center;font-family:"Audiowide",sans-serif;font-size:27px;color:#3a3a3a;padding-left:30px}
  .avg{left:1px;width:330px} .avg .grade-head{width:266px;background:linear-gradient(90deg,var(--red) 0 18px,var(--red-soft) 18px)}
  .good{left:384px;width:340px} .good .grade-head{width:300px;background:linear-gradient(90deg,var(--gold) 0 28px,var(--gold-soft) 28px);padding-left:52px}
  .great{left:788px;width:345px} .great .grade-head{width:342px;background:linear-gradient(90deg,var(--green) 0 28px,var(--green-soft) 28px);padding-left:36px}
  .habits{list-style:none;margin-top:25px;padding-left:14px}
  .habits li{position:relative;padding-left:26px;font-size:16.5px;line-height:19.5px;margin-bottom:19.5px}
  .habits li::before{content:"";position:absolute;left:0;top:3px;width:10px;height:10px;border:2px solid var(--muted);border-radius:50%;
    background:radial-gradient(circle,var(--muted) 0 2.5px,transparent 3px)}
  .habits li.plain::before{display:none}

  .avg .habits{width:330px}
  .good .habits{width:300px}
  .great .habits{width:344px}
  .tier-offense-nopuck .habits{padding-left:26px}
  .tier-offense-nopuck .avg .habits{width:300px}
  .tier-offense-nopuck .good .habits{width:322px}
  .tier-offense-nopuck .great .habits{width:330px}

  .tier-individual{top:753px;height:380px}
  .tier-offense-puck{top:1380px;height:364px}
  .tier-offense-nopuck{top:2004px;height:368px}
</style>
</head>
<body>

<header class="hero">
  <div class="hero-scene" role="img" aria-label="Photo of a lit hockey arena with a female player in a number 5 jersey seen from behind holding her helmet and stick"></div>
  <div class="hero-ice"></div>
  <h1 class="hero-title"><span class="line1">Hockey</span><span class="line2">Habits</span></h1>
</header>

<div class="pill pill-individual"><span class="pill-name">Individual</span></div>

<div class="skills skills-individual">
  <div class="skill" style="left:101px"><svg viewBox="0 0 56 56"><rect x="12" y="18" width="32" height="18" rx="6" transform="rotate(-35 28 27)"/><path d="M6 8l6 6M50 8l-6 6M6 48l6-6M50 48l-6-6" stroke="#e05858" stroke-width="3"/></svg><span class="skill-label">Compete</span></div>
  <div class="divider" style="left:203px"></div>
  <div class="skill" style="left:337px"><svg viewBox="0 0 56 56"><path d="M26 4c13 0 22 9 22 21 0 7-4 11-7 14v13H21v-7h-8v-10l-6-2 6-9C14 12 19 4 26 4z"/><path d="M28 14l8 3v6c0 5-4 8-8 9-4-1-8-4-8-9v-6z" fill="#fff"/></svg><span class="skill-label">Mentaltoughness</span></div>
  <div class="divider" style="left:491px"></div>
  <div class="skill" style="left:570px"><svg viewBox="0 0 56 56"><path d="M28 2c4 10 18 16 18 32a18 18 0 0 1-36 0c0-9 6-13 9-18 2 6 5 7 5 7 0-9 4-15 4-21z"/><rect x="20" y="30" width="16" height="14" rx="4" fill="#fff"/></svg><span class="skill-label">Spirit</span></div>
  <div class="divider" style="left:660px"></div>
  <div class="skill" style="left:742px"><svg viewBox="0 0 56 56"><path d="M4 52h48v-4H4zM8 46V34h8v12zM20 46V26h8v20zM32 46V18h8v28z"/><circle cx="44" cy="12" r="8"/></svg><span class="skill-label">Effort</span></div>
  <div class="divider" style="left:828px"></div>
  <div class="skill" style="left:926px"><svg viewBox="0 0 56 56"><circle cx="12" cy="14" r="5"/><circle cx="28" cy="12" r="5"/><circle cx="44" cy="14" r="5"/><path d="M6 22h12v30H6zM22 20h12v32H22zM38 22h12v30H38z"/></svg><span class="skill-label">Teamwork</span></div>
  <div class="divider" style="left:1032px"></div>
  <div class="skill" style="left:1128px"><svg viewBox="0 0 56 56"><path d="M28 8a15 15 0 0 1 9 27v6H19v-6a15 15 0 0 1 9-27z"/><rect x="21" y="44" width="14" height="5" rx="2"/><path d="M30 14l-8 12h6l-3 10 9-13h-6z" fill="#fff"/></svg><span class="skill-label">Hockey IQ</span></div>
</div>

<section class="tier tier-individual">
  <div class="tier-middle"></div>
  <div class="grade avg"><h2 class="grade-head">AVERAGE</h2>
    <ul class="habits">
      <li>Watches during games &amp; doesn't work hard in practice</li>
      <li>Gets easily upset with everyone</li>
      <li>ALL-IN when team is winning</li>
      <li>Works hard when they want to</li>
      <li>They should get me the puck</li>
      <li>Thinks they know hockey</li>
    </ul></div>
  <div class="grade good"><h2 class="grade-head">GOOD</h2>
    <ul class="habits">
      <li>Competes during games</li>
      <li>Park Mistakes (their's, teammates,<br>referees)</li>
      <li>ALL-IN during all games</li>
      <li>Works as hard as their opponents</li>
      <li class="plain">I'll pass if I have to</li>
      <li>Knows that they need to learn</li>
    </ul></div>
  <div class="grade great"><h2 class="grade-head">GREAT</h2>
    <ul class="habits">
      <li>Competes during games and practices</li>
      <li>Able to turn negative situations into positive<br>energy and use it!</li>
      <li>ALL-IN during practice and games</li>
      <li>Their effort matches the best of their ability -<br>they give 100% all the time!</li>
      <li>Enjoys setting up their teammates for an easy<br>goal as much as scoring!</li>
      <li>Watches GPHL, college, youth games trying to<br>always learn</li>
    </ul></div>
</section>

<div class="pill pill-offense-puck"><span class="pill-name">Offense w/ /Puck</span><span class="pill-note">You have the puck and your team is on offense</span></div>

<div class="skills skills-offense-puck">
  <div class="skill" style="left:134px"><svg viewBox="0 0 56 56"><circle cx="40" cy="8" r="6"/><path d="M30 16l12 4 6 10-4 2-5-7-6 10 8 8-4 4-10-9-8 10-6-3 10-14 2-9-6 2-4 6-4-2 6-9z"/><path d="M2 46l4 6h12" stroke="#c055e2" stroke-width="3" fill="none"/></svg><span class="skill-label">Skating with the puck</span></div>
  <div class="divider" style="left:288px"></div>
  <div class="skill" style="left:406px"><svg viewBox="0 0 56 56"><path d="M8 6l6-4 24 30-6 6zM48 6l-6-4-24 30 6 6z"/><rect x="10" y="34" width="36" height="6" rx="3"/><ellipse cx="28" cy="50" rx="8" ry="4"/></svg><span class="skill-label">Stickhandling</span></div>
  <div class="divider" style="left:527px"></div>
  <div class="skill" style="left:644px"><svg viewBox="0 0 56 56"><path d="M6 50c0-20 12-30 30-30V10l16 16-16 16V32C22 32 12 38 6 50z"/></svg><span class="skill-label">Making a pass</span></div>
  <div class="divider" style="left:768px"></div>
  <div class="skill" style="left:862px"><svg viewBox="0 0 56 56"><path d="M4 16l6-4 18 24h8v8H22z"/><ellipse cx="44" cy="40" rx="6" ry="4"/><path d="M40 22l8-8M46 28h8M40 12l4 8" stroke="#c055e2" stroke-width="3"/></svg><span class="skill-label">Shooting</span></div>
  <div class="divider" style="left:960px"></div>
  <div class="skill" style="left:1070px"><svg viewBox="0 0 56 56"><circle cx="28" cy="44" r="9"/><path d="M26 34V12h-6l8-10 8 10h-6v22zM22 32L10 20l-4 5V12h13l-5 4 12 12zM34 32l12-12 4 5V12H37l5 4-12 12z"/></svg><span class="skill-label">Play &nbsp;Making</span></div>
</div>

<section class="tier tier-offense-puck">
  <div class="tier-middle"></div>
  <div class="grade avg"><h2 class="grade-head">AVERAGE</h2>
    <ul class="habits">
      <li>Eyes always on the puck</li>
      <li>Control puck in front of body</li>
      <li>Blindly hitting the puck</li>
      <li>Shoots towards the net wherever they are</li>
      <li>Making a deke, pass or shot<br>once D is on you</li>
    </ul></div>
  <div class="grade good"><h2 class="grade-head">GOOD</h2>
    <ul class="habits">
      <li>Eyes on puck see game in peripheral<br>vision</li>
      <li>Control puck side to side</li>
      <li>Making a pass toward teammate</li>
      <li>Shoots hard towards the net</li>
      <li>Making a deke, pass or shot before the<br>D is on you</li>
    </ul></div>
  <div class="grade great"><h2 class="grade-head">GREAT</h2>
    <ul class="habits">
      <li>Eyes on the game peripheral vision for puck</li>
      <li>Control puck in all positions</li>
      <li>Make a pass with eyes up tape to tape to<br>where the player is going</li>
      <li>Finds a good shooting lane and shoots as hard<br>as they possibly can</li>
      <li>Anticipate the play and play in areas D can't<br>get you</li>
    </ul></div>
</section>

<div class="pill pill-offense-nopuck"><span class="pill-name">Offense w/o /Puck</span><span class="pill-note">You do not have the puck but your teammate does</span></div>

<div class="skills skills-offense-nopuck">
  <div class="skill" style="left:105px"><svg viewBox="0 0 56 56"><path d="M4 14l6-4 18 24h8v8H22z"/><rect x="38" y="30" width="14" height="12" rx="3"/></svg><span class="skill-label">Receiving a pass</span></div>
  <div class="divider" style="left:190px"></div>
  <div class="skill" style="left:312px"><svg viewBox="0 0 56 56"><rect x="2" y="4" width="44" height="32" rx="3"/><path d="M10 10l10 10M38 10L28 20M10 30l10-10M38 30L28 20" stroke="#fff" stroke-width="3"/><circle cx="44" cy="42" r="10"/><path d="M39 42l4 4 6-7" stroke="#fff" stroke-width="3" fill="none"/></svg><span class="skill-label">Rebounds, tips, screens</span></div>
  <div class="divider" style="left:432px"></div>
  <div class="skill" style="left:516px"><svg viewBox="0 0 56 56"><circle cx="24" cy="24" r="17" fill="none" stroke="#4c86e2" stroke-width="5"/><path d="M36 36l14 14" stroke="#4c86e2" stroke-width="6"/><path d="M16 24l6 6 10-11" stroke="#4c86e2" stroke-width="4" fill="none"/></svg><span class="skill-label">Finding open ice</span></div>
  <div class="divider" style="left:600px"></div>
  <div class="skill" style="left:757px"><svg viewBox="0 0 56 56"><circle cx="28" cy="10" r="7"/><rect x="20" y="20" width="16" height="22" rx="5"/><ellipse cx="28" cy="46" rx="20" ry="7" fill="none" stroke="#4c86e2" stroke-width="4"/></svg><span class="skill-label">Positioning (traditional roles)</span></div>
  <div class="divider" style="left:912px"></div>
  <div class="skill" style="left:1048px"><svg viewBox="0 0 56 56"><path d="M4 14h26V6l14 14-14 14v-8H4zM52 42H26v8L12 36l14-14v8h26z"/></svg><span class="skill-label">Ready to switch to defense</span></div>
</div>

<section class="tier tier-offense-nopuck">
  <div class="tier-middle"></div>
  <div class="grade avg"><h2 class="grade-head">AVERAGE</h2>
    <ul class="habits">
      <li>Eyes always on the puck</li>
      <li>Control puck in front of body</li>
      <li>Blindly hitting the puck</li>
      <li>Shoots towards the net wherever<br>they are</li>
      <li>Making a deke, pass or shot<br>once D is on you</li>
    </ul></div>
  <div class="grade good"><h2 class="grade-head">GOOD</h2>
    <ul class="habits">
      <li>Eyes on puck see game in peripheral<br>vision</li>
      <li>Control puck side to side</li>
      <li>Making a pass toward teammate</li>
      <li>Shoots hard towards the net</li>
      <li>Making a deke, pass or shot before the<br>D is on you</li>
    </ul></div>
  <div class="grade great"><h2 class="grade-head">GREAT</h2>
    <ul class="habits">
      <li>Eyes on the game peripheral vision for puck</li>
      <li>Control puck in all positions</li>
      <li>Make a pass with eyes up tape to tape to<br>where the player is going</li>
      <li>Finds a good shooting lane and shoots as<br>hard as they possibly can</li>
      <li>Anticipate the play and play in areas D can't<br>get you</li>
    </ul></div>
</section>

</body>
</html>
```